Custom Graphic Design For Online Shopping Service Homepage

We need a graphic design for the homepage of our company website. This is the 1st image for the slideshow module on the homepage that will require only 1 graphic with a continuous background for the other slideshows. So a psd file with the background image and content image.
This is a multi-part project and selected individual(s) will be invited to participate in next assignments for future web/graphic designs.

Our company is called 'BuyNorthway.com' where we provide an online personal shopping service where we shop for customers and provide quality service. The central theme should be to get the cheapest prices online while getting the best in-store type shopping experience.

The design chosen will be something that has a unique style and represents our company logo the best.
The main focus will be to have the image represent the "future of online shopping" with a personalized touch and lesson. Something friendly but not just random people smiling at you that make you think we're selling products.
Some ideas for the image would be like an internet shopping concept, a shopping mall that's help you shop, a professional shopper equates to saving time and money.
http://www.layoutfoundry.example/demo/58214.html
This is more of the content and background matching for the slideshow. A current screenshot of the site is shown with the black area the requirements.
Updates

Project Deadline Extended
Reason: allow for more time to design image due to change

The menu top has changed to an interactive tidal menu with the logo on the top left corner.
http://demo.brightaddons.example/tidal-menu.html

I wouldn't worry too much about matching font colors for the background, i just need the proper background color to match the menu and slideshow content.  A lighter color seems to fit the style better.  I have attached a preview of what I need in the black.  Please ignore extra content from the page since a web design is not needed but a content design for the slideshow.

The payment is now guaranteed and I have upped the first place prize $20 to $200 for extending the job.

A better example would be this slideshow with the content matching background.
We apologize for the requirements for the design.

Target Market(s)

Online shoppers that don't have time to shop, people who want to save money, less tech-savy shoppers

Industry/Entity Type

Graphic Design

Requirements
Must have
• 1 continuous background in slideshow and 1 content image inside
The background is very important because it will be used for the next 3 images.
http://www.velmore.example/ - This is the size background we want, not exactly the style and color though.
http://www.quillguard.example/
Nice to have
• We have a logo but it does not need to be displayed into the graphic(optional). Could be good as a reference but the logo for now will be next to the menu on the top left like the velmore design.
Should not have
• Buttons and menus, they will be added for the web design project.

```html
<!DOCTYPE html>
<html lang="en">
<head>
<meta charset="utf-8">
<title>BuyNorthway.com – Online Personal Shopping</title>
<link rel="stylesheet" href="https://fonts.googleapis.com/css2?family=Maven+Pro:wght@400;500;700&family=Titillium+Web:wght@300&family=Ubuntu:wght@400;500;700&family=Roboto:wght@400&display=swap">
<style>
  :root {
    --header-bg: #e8e8e8;
    --nav-green: #6a9a1a;
    --nav-orange: #e8891a;
    --nav-red: #8e2020;
    --nav-teal: #3aa8bf;
    --nav-purple: #4d3f7a;
    --nav-maroon: #8a2424;
    --hero-orange: #f25c05;
    --hero-amber: #fb9a0c;
    --hero-yellow: #f4d100;
    --hero-lime: #b8e416;
    --arrow-bg: #4a3a14;
    --button-blue: #1a8fe0;
    --ink-dark: #0f3a4d;
    --ink-body: #333333;
    --ink-title: #2d3b44;
    --icon-grey: #9a9fa4;
    --rule: #e2e6e8;
    --white: #ffffff;
  }
  * { box-sizing: border-box; margin: 0; padding: 0; }
  html, body { width: 1200px; height: 670px; overflow: hidden; background: var(--white); }
  body { position: relative; font-family: "Roboto", Arial, sans-serif; }

  .site-header { position: absolute; left: 0; top: 0; width: 1200px; height: 102px; background: var(--header-bg); }
  .brand { position: absolute; left: 258px; top: 52px; display: flex; align-items: center; gap: 7px; }
  .brand-mark { width: 12px; height: 12px; border-radius: 50%; background: var(--nav-orange); }
  .brand-name { font-family: "Maven Pro", sans-serif; font-weight: 700; font-size: 19px; color: var(--nav-orange); }

  .main-nav { position: absolute; left: 0; top: 0; width: 1200px; height: 102px; }
  .nav-item { position: absolute; top: 64px; width: 88px; margin-left: -44px; text-align: center;
    font-family: "Ubuntu", sans-serif; font-weight: 700; font-size: 11.2px; white-space: nowrap; }
  .nav-tab { position: absolute; top: 90px; width: 77px; margin-left: -38px; height: 13px;
    border: 2px solid var(--white); border-bottom: none; border-radius: 6px 6px 0 0; }

  .hero { position: absolute; left: 0; top: 102px; width: 1200px; height: 349px;
    background: linear-gradient(90deg, var(--hero-orange) 0%, #f77a08 30%, var(--hero-amber) 55%, var(--hero-yellow) 75%, var(--hero-lime) 92%, #9cd82a 100%); overflow: hidden; }
  .hero-glow { position: absolute; inset: 0;
    background: radial-gradient(ellipse at 30% 60%, rgba(255,200,60,0.35), transparent 55%),
                linear-gradient(180deg, rgba(200,40,0,0.18), transparent 40%, rgba(255,255,255,0.08)); }
  .hero-title { position: absolute; left: 203px; top: 36px; width: 340px;
    font-family: "Titillium Web", sans-serif; font-weight: 300; font-size: 37px; line-height: 44px; color: var(--white); }
  .hero-text { position: absolute; left: 203px; top: 140px; width: 296px;
    font-family: "Ubuntu", sans-serif; font-size: 10.2px; line-height: 19px; color: #4a2200; }
  .hero-button { position: absolute; left: 203px; top: 216px; width: 138px; height: 36px; border-radius: 3px;
    background: var(--button-blue); color: var(--white); font-family: "Ubuntu", sans-serif; font-weight: 500;
    font-size: 14px; line-height: 36px; text-align: center; box-shadow: 0 2px 4px rgba(0,0,0,0.2); }
  .hero-dots { position: absolute; left: 205px; top: 283px; display: flex; gap: 9px; }
  .hero-dot { width: 10px; height: 10px; border-radius: 50%; background: var(--white); }
  .hero-dot.is-active { background: #3a2a10; }
  .hero-arrow { position: absolute; top: 144px; width: 26px; height: 26px; background: var(--arrow-bg); }
  .hero-arrow.prev { left: 154px; }
  .hero-arrow.next { left: 957px; }
  .hero-visual { position: absolute; left: 556px; top: 48px; width: 342px; height: 266px;
    border: 2px solid var(--white); background: linear-gradient(135deg, #8a98a6 0%, #6c7a88 55%, #4f5c6a 100%);
    box-shadow: 0 4px 10px rgba(0,0,0,0.2); }

  .intro { position: absolute; left: 72px; top: 451px; width: 1056px; height: 80px;
    background: linear-gradient(180deg, rgba(225,240,246,0.7), rgba(255,255,255,0)); }
  .intro-heading { position: absolute; left: 216px; top: 473px; width: 752px; text-align: center;
    font-family: "Maven Pro", sans-serif; font-weight: 500; font-size: 16.5px; color: var(--ink-dark); letter-spacing: 0.3px; }
  .intro-rule { position: absolute; left: 216px; top: 514px; width: 752px; height: 2px; background: var(--rule); }

  .feature { position: absolute; width: 240px; }
  .feature-title { font-family: "Maven Pro", sans-serif; font-weight: 400; font-size: 16px; line-height: 20px; color: var(--ink-title); letter-spacing: 0.2px; white-space: nowrap; }
  .feature-icon { position: absolute; left: 0; top: 32px; }
  .feature-text { position: absolute; left: 38px; top: 29px; width: 200px; font-size: 9.8px; line-height: 16.4px; color: var(--ink-body); }
</style>
</head>
<body>
  <header class="site-header">
    <div class="brand"><span class="brand-mark"></span><span class="brand-name">BuyNorthway.com</span></div>
    <nav class="main-nav">
      <span class="nav-item" style="left:514px;color:var(--nav-green)">ABOUT US</span>
      <span class="nav-item" style="left:602px;color:var(--nav-orange)">FEATURES</span>
      <span class="nav-item" style="left:690px;color:var(--nav-red)">PRICES</span>
      <span class="nav-item" style="left:778px;color:var(--nav-teal)">BLOG</span>
      <span class="nav-item" style="left:866px;color:var(--nav-purple)">CONTACT US</span>
      <span class="nav-item" style="left:954px;color:var(--nav-maroon)">MEMBERS</span>
      <span class="nav-tab" style="left:516px;background:var(--nav-green)"></span>
      <span class="nav-tab" style="left:604px;background:var(--nav-orange)"></span>
      <span class="nav-tab" style="left:692px;background:var(--nav-red)"></span>
      <span class="nav-tab" style="left:780px;background:var(--nav-teal)"></span>
      <span class="nav-tab" style="left:868px;background:var(--nav-purple)"></span>
      <span class="nav-tab" style="left:956px;background:var(--nav-maroon)"></span>
    </nav>
  </header>

  <section class="hero">
    <div class="hero-glow"></div>
    <h1 class="hero-title">An online personal shopping service</h1>
    <p class="hero-text">We shop for customers and provide quality service. The central theme should be to get the cheapest prices online while getting the best in-store type shopping experience.</p>
    <div class="hero-button">Find out more</div>
    <div class="hero-dots"><span class="hero-dot is-active"></span><span class="hero-dot"></span><span class="hero-dot"></span></div>
    <div class="hero-arrow prev"><svg width="26" height="26" viewBox="0 0 26 26"><path d="M15 8 L10 13 L15 18" fill="none" stroke="#fff" stroke-width="2.5"/></svg></div>
    <div class="hero-arrow next"><svg width="26" height="26" viewBox="0 0 26 26"><path d="M11 8 L16 13 L11 18" fill="none" stroke="#fff" stroke-width="2.5"/></svg></div>
    <div class="hero-visual" role="img" aria-label="Photo of a young shopper touching a floating shopping-cart icon surrounded by sale badges on a grey-blue background"></div>
  </section>

  <div class="intro"></div>
  <h2 class="intro-heading">FUNCTIONAL AND AWESOME LUMORA, PAGELEAF AND HTML TEMPLATES FOR EVERYONE.</h2>
  <div class="intro-rule"></div>

  <article class="feature" style="left:216px;top:542px">
    <h3 class="feature-title">12-COL GRID SYSTEM</h3>
    <svg class="feature-icon" width="26" height="28" viewBox="0 0 26 28" fill="var(--icon-grey)">
      <rect x="0" y="0" width="26" height="3"/><rect x="0" y="7" width="18" height="3"/><rect x="0" y="14" width="26" height="3"/>
      <rect x="0" y="23" width="3" height="3"/><rect x="6" y="23" width="3" height="3"/><rect x="12" y="23" width="3" height="3"/>
    </svg>
    <p class="feature-text">Our templates use the popular 12col.css framework which makes developing much easier and enjoying.</p>
  </article>
  <article class="feature" style="left:472px;top:542px">
    <h3 class="feature-title">COST EFFECTIVE</h3>
    <svg class="feature-icon" width="26" height="28" viewBox="0 0 26 28"><path d="M0 0 H12 L26 14 L14 26 L0 12 Z" fill="var(--icon-grey)"/><circle cx="6" cy="6" r="2.5" fill="#fff"/></svg>
    <p class="feature-text">These templates are truly some great deals! They include so many features for a relatively small amount of money.</p>
  </article>
  <article class="feature" style="left:728px;top:542px">
    <h3 class="feature-title">TECHNICAL SUPPORT</h3>
    <svg class="feature-icon" width="26" height="28" viewBox="0 0 26 28" fill="none" stroke="var(--icon-grey)" stroke-width="3">
      <rect x="2" y="2" width="14" height="10" rx="5"/><rect x="10" y="12" width="14" height="10" rx="5"/><path d="M6 12 L5 18"/>
    </svg>
    <p class="feature-text">Problems? Don't worry!! One of the biggest advantage of our templates is the technical support system. Let us know!</p>
  </article>
  <article class="feature" style="left:216px;top:646px"><h3 class="feature-title">TIME SAVING</h3></article>
  <article class="feature" style="left:472px;top:646px"><h3 class="feature-title">BROWSER COMPATIBILITY</h3></article>
  <article class="feature" style="left:728px;top:646px"><h3 class="feature-title">MOBILE FRIENDLY</h3></article>
</body>
</html>
```